Etiketten-Design für Glühwein/Kinderpunsch
Zielgruppe
wir sind ein konventioneller Landwirtschaftlicher Betrieb. Ein Standbein sind unsere 2ha große Heidelbeerplantage. wir haben eine 'beerige Produktpalette' und brauchen für die Saisonware Glühwein/Kinderpunsch neue Etiketten; Zielgruppe: Regionale Vermarkung, Direktvermakrtung, von 0-99,
Aufgabenstellung
peppiges, auffälliges Etiektt, das Lust auf Glühwein/Winter macht und für den alkoholfreie Fruchtpunsch was das Kinder und Erwachsene anspricht
Flaschenetiektt mit den gesetzlichen Vorgaben,
Farben: Unser Logo ist in Lila, hellgrün, dunkelgrün, schwarz und weiß gehalten, sind aber prinzipiell offen für alles

```html
<!DOCTYPE html>
<html lang="de">
<head>
<meta charset="utf-8">
<title>Brambeck Hofgenuss – Etiketten Glühwein &amp; Kinderpunsch</title>
<link rel="stylesheet" href="https://fonts.googleapis.com/css2?family=Fira+Sans+Extra+Condensed:wght@700;800&display=swap">
<style>
  :root {
    --page: #ffffff;
    --stripe-light: #ffffff;
    --berry-label: #9d8bcf;
    --berry-ink: #5e2f8f;
    --berry-art: #9479c8;
    --berry-art-soft: #c4b4e8;
    --punch-label: #f3a46d;
    --punch-ink: #c4561a;
    --punch-art: #d9895a;
    --punch-art-soft: #f2c5a4;
    --brand-ink: #5e2f8f;
  }
  * { box-sizing: border-box; margin: 0; padding: 0; }
  html, body {
    width: 944px;
    height: 1200px;
    overflow: hidden;
    background: var(--page);
  }
  .canvas {
    position: relative;
    width: 944px;
    height: 1200px;
    display: flex;
    justify-content: center;
    align-items: center;
    gap: 40px;
  }
  .label {
    position: relative;
    width: 420px;
    height: 430px;
    overflow: hidden;
    background: repeating-linear-gradient(90deg,
      var(--stripe) 0 3.4px,
      var(--stripe-light) 3.4px 5px);
  }
  .label--gluehwein { --stripe: var(--berry-label); --ink: var(--berry-ink); --art: var(--berry-art); --art-soft: var(--berry-art-soft); }
  .label--punsch { --stripe: var(--punch-label); --ink: var(--punch-ink); --art: var(--punch-art); --art-soft: var(--punch-art-soft); }

  .brand {
    position: absolute;
    top: 122px;
    left: 0;
    width: 100%;
    display: flex;
    justify-content: center;
    align-items: center;
    gap: 10px;
  }
  .brand__dot {
    width: 16px;
    height: 16px;
    border-radius: 50%;
    background: var(--brand-ink);
  }
  .brand__name {
    font-family: "Fira Sans Extra Condensed", sans-serif;
    font-weight: 800;
    font-size: 44px;
    line-height: 1;
    color: var(--brand-ink);
  }

  .art-mug {
    position: absolute;
    left: 6px;
    top: 208px;
    width: 140px;
    height: 160px;
    border-radius: 16px 16px 44px 44px;
    background: linear-gradient(160deg, var(--art-soft), var(--art));
  }
  .art-cookies {
    position: absolute;
    left: 338px;
    top: 196px;
    width: 78px;
    height: 96px;
    border-radius: 40% 40% 22% 22%;
    background: linear-gradient(170deg, var(--art-soft), var(--art));
  }

  .product {
    position: absolute;
    font-family: "Fira Sans Extra Condensed", sans-serif;
    color: var(--ink);
    line-height: 1;
    text-transform: uppercase;
    white-space: nowrap;
  }
  .product__kind { font-weight: 700; letter-spacing: 0.5px; }
  .product__name { font-weight: 800; }

  .label--gluehwein .product__kind { left: 206px; top: 279px; font-size: 26px; }
  .label--gluehwein .product__name { left: 160px; top: 306px; font-size: 60px; }
  .label--punsch .product__kind { left: 160px; top: 276px; font-size: 34px; }
  .label--punsch .product__name { left: 156px; top: 312px; font-size: 66px; }
</style>
</head>
<body>
<main class="canvas">
  <section class="label label--gluehwein">
    <div class="brand">
      <span class="brand__dot"></span>
      <span class="brand__name">Brambeck Hofgenuss</span>
    </div>
    <div class="art-mug" role="img" aria-label="Illustration: lila Tasse mit Schneeflocke, Orangenscheibe und Zimtstange"></div>
    <div class="art-cookies" role="img" aria-label="Illustration: lila Lebkuchen in Tannenbaum- und Sternform"></div>
    <p class="product product__kind">Heidelbeer</p>
    <p class="product product__name">Glühwein</p>
  </section>

  <section class="label label--punsch">
    <div class="brand">
      <span class="brand__dot"></span>
      <span class="brand__name">Brambeck Hofgenuss</span>
    </div>
    <div class="art-mug" role="img" aria-label="Illustration: orange Tasse mit Schneeflocke, Orangenscheibe und Zimtstange"></div>
    <div class="art-cookies" role="img" aria-label="Illustration: Lebkuchen in Tannenbaum- und Sternform"></div>
    <p class="product product__kind">Kinder</p>
    <p class="product product__name">Punsch</p>
  </section>
</main>
</body>
</html>
```